Hamlet Pantry Brand Presentation

Looking for a brand presentation for Hamlet Pantry. A business with three stores in Hackney, Clapham and Kings Cross and two booming e-commerce sites www.larderkiste.co.uk and www.meadowvitalcrate.co.uk.

The presentation should highlight the two online brands under the Hamlet Pantry umbrella- MeadowVitalCrate and LarderKiste- as well as Hamlet Pantry itself.

The presentation should give an overview of the history of the business, how fast it is growing and highlight the potential for growth.

Starting as a family run store, Hamlet Greens, in Hackney 7 years ago we have now expanded to 3 stores and 2 online sites with a turnover of 4m a year as well as collaborating with leading brands in the health foods sector such as Brightly Maren, Petras Cacaoberry, Plump Pulse co and Vyra.

The presentation should present us as a challenger to highstreet stores with a selective eye for incubating up and coming brands and providing high quality produce and products to our customer. It should also highlight the benefits of independent chains, we have communities around our stores of customers and brands.

Please include our positive attitude to sustainability: we run saved-plate-club in all our stores, have purelo refil stations, make our own juice out of wonky fruit and are selective in working with innivotive, ethical and eco-friendly brands.

Add a section on customer demographics. Mention that across our stores we have a wide range of customers: young professionals, gym/health consicious coming in for supplements & protein, young families focussed on healthy living buying baby food, fresh fruit & veg, young foodies.

We have plans to expand our London locations and would like this deck to help us compete with locations highstreet brands are fighting for. We also plan to start our own production facilities, making branded 'LarderKiste' storecupboard health foods.
Ideally encorporate the colours green and orange into the deck to match our logo. Please include some data on the health food sector, it is growing year on year, and customers wanting to shop local.

Please look at the attached pdf draft deck for more information on the business and do not hesitate to get in touch if you have any questions/require anything more from us.

Target Market(s)

Suppliers, financial constitutions, brands, investors

Industry/Entity Type

Retail

Font styles to use
Serif

Colors
00AB8E
00BBA5
67D7C9
C6EFE9
E9F9F6
F0912C
F2A743
F7CA91
FBE8D2
FDF5EE

Requirements
Must have
• Photos of the three stores, websites & their domain names

```html
<!DOCTYPE html>
<html lang="en">
<head>
<meta charset="utf-8">
<title>Hamlet Pantry – Brand Presentation</title>
<link rel="stylesheet" href="https://fonts.googleapis.com/css2?family=Bebas+Neue&family=Montserrat:wght@400;500;600&display=swap">
<style>
  :root {
    --backdrop: #d9d9d9;
    --paper: #ffffff;
    --brand-green: #0f5436;
    --brand-orange: #f0912c;
    --deep-green: #0d5240;
    --ink: #2a2a2a;
  }
  * { margin: 0; padding: 0; box-sizing: border-box; }
  html, body { width: 917px; height: 1200px; overflow: hidden; background: var(--backdrop); }
  .stage {
    width: 960px; height: 1256px; position: relative;
    transform: scale(0.9552); transform-origin: 0 0;
  }
  .slide {
    position: absolute; left: 115px; width: 730px; height: 564px;
    background: var(--paper); overflow: hidden;
    box-shadow: 0 4px 14px rgba(0,0,0,0.28);
  }
  .slide--cover { top: 46px; }
  .slide--about { top: 645px; height: 563px; }

  .brand-lockup { position: absolute; display: flex; align-items: center; gap: 7px; }
  .brand-lockup__mark { background: var(--brand-green); flex: none; }
  .brand-lockup__name {
    font-family: "Montserrat", sans-serif; font-weight: 500; color: var(--brand-green);
    letter-spacing: 0.5px; line-height: 1;
  }
  .slide--cover .brand-lockup { left: 0; right: 0; top: 62px; justify-content: center; }
  .slide--cover .brand-lockup__mark { width: 30px; height: 30px; }
  .slide--cover .brand-lockup__name { font-size: 30px; }
  .slide--about .brand-lockup { left: 58px; top: 58px; }
  .slide--about .brand-lockup__mark { width: 24px; height: 24px; }
  .slide--about .brand-lockup__name { font-size: 23px; }

  .cover-title {
    position: absolute; left: 0; right: 0; top: 143px; text-align: center;
    font-family: "Bebas Neue", sans-serif; font-weight: 400; font-size: 78px; line-height: 1; letter-spacing: 0.5px;
  }
  .cover-title__lead { color: var(--brand-green); }
  .cover-title__tail { color: var(--brand-orange); }

  .cover-photo {
    position: absolute; left: 0; top: 246px; width: 730px; height: 318px;
    background: linear-gradient(180deg, #a9c98a 0%, #7da55a 35%, #5c6a3e 52%, #b83a22 72%, #8e2415 100%);
  }
  .cover-cut { position: absolute; left: 0; top: 246px; width: 730px; height: 60px; }

  .about-photo {
    position: absolute; left: 0; top: 150px; width: 730px; height: 413px;
    background:
      linear-gradient(180deg, #ffffff 0%, #ffffff 8%, rgba(255,255,255,0.85) 30%, rgba(255,255,255,0) 72%),
      linear-gradient(90deg, #6fae7c 0%, #3f8f5a 30%, #9fbf6a 60%, #7f9f4f 100%);
  }
  .about-shapes { position: absolute; left: 0; top: 0; width: 730px; height: 130px; }
  .about-title {
    position: absolute; left: 52px; top: 166px;
    font-family: "Bebas Neue", sans-serif; font-weight: 400; font-size: 54px; line-height: 1; color: var(--brand-orange);
  }
  .about-copy {
    position: absolute; left: 52px; top: 229px; width: 628px;
    font-family: "Montserrat", sans-serif; font-size: 12.6px; line-height: 16.5px;
    color: var(--ink); text-align: justify;
  }
</style>
</head>
<body>
<main class="stage">

  <section class="slide slide--cover">
    <div class="brand-lockup">
      <span class="brand-lockup__mark"></span>
      <span class="brand-lockup__name">LARDERKISTE</span>
    </div>
    <h1 class="cover-title"><span class="cover-title__lead">HAMLET</span> <span class="cover-title__tail">PANTRY</span></h1>
    <div class="cover-photo" role="img" aria-label="Market stall with baskets of cabbages, lettuce and red tomatoes with chalk price tags"></div>
    <svg class="cover-cut" viewBox="0 0 730 60" aria-hidden="true">
      <polygon points="240,0 730,0 730,48 285,48" fill="var(--paper)"/>
      <polygon points="255,14 730,14 730,32 268,32" fill="var(--brand-orange)"/>
    </svg>
  </section>

  <section class="slide slide--about">
    <div class="about-photo" role="img" aria-label="Market table with green beans, aubergines and cucumbers on green cloth, softly faded"></div>
    <svg class="about-shapes" viewBox="0 0 730 130" aria-hidden="true">
      <polygon points="323,0 412,0 497,107 425,125" fill="var(--brand-orange)"/>
      <polygon points="415,0 730,0 730,73 510,125" fill="var(--deep-green)"/>
    </svg>
    <div class="brand-lockup">
      <span class="brand-lockup__mark"></span>
      <span class="brand-lockup__name">LARDERKISTE</span>
    </div>
    <h2 class="about-title">WHO ARE WE?</h2>
    <p class="about-copy">Over the past 10 years we have grown from a humble family-run organic grocers in Hackney to a wholefoods business with three London locations and two online platforms. Our ethos throughout this growth has remained focused on providing healthy, well-made, well-grown food to our customers as well as working with the most exciting small brands in the sector.</p>
  </section>

</main>
</body>
</html>
```